New Construction company looking for powerful bold logo. people see the logo, leaves an impression

We need a business card for our new company. We provide site work for commercial projects in South Texas. We clear land, excavation, run under ground utilities, concrete work, dirt work etc. We like the black card. I created a webpage www.tarn-vbuilders.com .... As I grow with projects I will put up pictures with video, and intro music. Want it look cool, bold, powerful, and slick looking. Creating 'TVB'....as my logo (possibly or if you have something you want to have fun with). Just have fun!!....thank you!

Dorian Pruett Business Manager Serving South Texas PO Box 4837 Robstown,TX. 78380 Mobile: 361-752-6083 www.tarn-vbuilders.com dorian@tarn-vbuilders.com you can put this anyway you see fit in your design and layout. thank you

Target Market(s)

General Contractors; Home Builders;

Industry/Entity Type

Construction

Contact Information for Business Card

I want the card to be black.

Font styles to use
Other font styles liked:
• Designer choice

Requirements
Must have
• Tarn-V Construction
• Site Work - Utilities/Concrete/Pad/Grading/Excavation (on the back side)
Nice to have
• Maybe TVB as the logo.....or just a symbol that would be TV.....and then construction to tie it togther...

```html
<!DOCTYPE html>
<html lang="en">
<head>
<meta charset="utf-8">
<title>Tarn-V Construction — Business Card</title>
<link rel="stylesheet" href="https://fonts.googleapis.com/css2?family=Open+Sans:wght@400;600;700&family=Roboto+Condensed:wght@400&display=swap">
<style>
  :root {
    --backdrop: #e9e6e2;
    --card: #ffffff;
    --ink: #231f20;
    --muted: #555555;
    --accent: #f4a21d;
    --band-text: #231f20;
  }
  * { margin: 0; padding: 0; box-sizing: border-box; }
  html, body { width: 1200px; height: 1000px; overflow: hidden; }
  body {
    background: var(--backdrop);
    font-family: "Open Sans", Arial, sans-serif;
    position: relative;
  }
  .card {
    position: absolute;
    left: 266px;
    width: 667px;
    background: var(--card);
    box-shadow: 3px 4px 8px rgba(0,0,0,0.35);
    overflow: hidden;
  }
  .card--front { top: 102px; height: 381px; }
  .card--back  { top: 520px; height: 380px; }

  .brand {
    position: absolute;
    display: flex;
    align-items: center;
  }
  .brand__mark { background: var(--accent); flex: none; }
  .brand__name {
    font-weight: 700;
    color: var(--ink);
    white-space: nowrap;
    line-height: 1;
  }
  .card--front .brand { left: 62px; top: 46px; gap: 12px; }
  .card--front .brand__mark { width: 42px; height: 42px; }
  .card--front .brand__name { font-size: 22px; }

  .card--back .brand { left: 0; right: 0; top: 110px; justify-content: center; gap: 18px; }
  .card--back .brand__mark { width: 66px; height: 66px; }
  .card--back .brand__name { font-size: 34px; }

  .person { position: absolute; left: 432px; top: 146px; }
  .person__name { font-size: 22px; font-weight: 700; color: var(--ink); letter-spacing: 0.2px; }
  .person__role { font-size: 15px; color: var(--muted); margin-top: 2px; }

  .contact { position: absolute; left: 432px; top: 222px; list-style: none; }
  .contact__item {
    display: flex; align-items: center; gap: 10px;
    font-size: 15px; color: var(--muted); height: 27px;
  }
  .contact__icon { width: 16px; height: 16px; flex: none; }

  .tagline {
    position: absolute; left: 59px; top: 260px;
    font-size: 15px; line-height: 23px; color: var(--muted);
  }

  .front-bands { position: absolute; left: 0; top: 0; }

  .services {
    position: absolute; left: 0; right: 0; top: 308px; height: 37px;
    background: var(--accent);
    border-top: 3px solid var(--ink);
    border-bottom: 3px solid var(--ink);
    display: flex; align-items: center; justify-content: center; gap: 10px;
    list-style: none;
    font-family: "Roboto Condensed", "Arial Narrow", sans-serif;
    font-size: 20px; color: var(--band-text);
  }
  .services li::before { content: "•"; color: #ffffff; margin-right: 5px; }
</style>
</head>
<body>

  <section class="card card--front">
    <div class="brand">
      <span class="brand__mark"></span>
      <span class="brand__name">Tarn-V Construction</span>
    </div>

    <div class="person">
      <p class="person__name">PERSON NAME</p>
      <p class="person__role">Designation</p>
    </div>

    <ul class="contact">
      <li class="contact__item">
        <svg class="contact__icon" viewBox="0 0 16 16"><rect x="2" y="1" width="12" height="14" rx="2" fill="var(--ink)"/><rect x="4" y="3" width="8" height="9" fill="#fff"/><path d="M5 11 L11 4" stroke="var(--ink)" stroke-width="1.4"/></svg>
        <span>123 456 7890</span>
      </li>
      <li class="contact__item">
        <svg class="contact__icon" viewBox="0 0 16 16"><path d="M1 6 L8 1 L15 6 V15 H1 Z" fill="var(--ink)"/><path d="M3 7 L8 11 L13 7" stroke="#fff" stroke-width="1.4" fill="none"/></svg>
        <span>info@example.com</span>
      </li>
      <li class="contact__item">
        <svg class="contact__icon" viewBox="0 0 16 16"><path d="M3 15 L3 8 L9 8 L9 4 L15 9 L9 14 L9 11 L6 11 L6 15 Z" fill="var(--ink)"/></svg>
        <span>www.example.com</span>
      </li>
    </ul>

    <p class="tagline">Consectetur adipiscing elit.<br>Donec accumsan.</p>

    <svg class="front-bands" width="667" height="381" viewBox="0 0 667 381" aria-hidden="true">
      <path d="M341 338 L667 338 L667 353 L346 353 Z" fill="var(--accent)"/>
      <path d="M0 327 L329 327 Q336 327 339 333 L347 353 L667 353 L667 381 L0 381 Z" fill="var(--ink)"/>
    </svg>
  </section>

  <section class="card card--back">
    <div class="brand">
      <span class="brand__mark"></span>
      <span class="brand__name">Tarn-V Construction</span>
    </div>

    <ul class="services">
      <li>Utilities</li>
      <li>Concrete</li>
      <li>Pad</li>
      <li>Grading</li>
      <li>Excavation</li>
    </ul>
  </section>

</body>
</html>
```